Buch-Cover für Buch aus den Bereichen Persönlichkeitsentwicklung/ Ratgeber für Erfolg, moderne Spiritualität
Buch-Cover für Buch aus den Bereichen Persönlichkeitsentwicklung/ Ratgeber für Erfolg, moderne ..

```html
<!DOCTYPE html>
<html lang="de">
<head>
<meta charset="utf-8">
<title>Sunny Mind Manifestieren – Buchumschlag</title>
<link href="https://fonts.googleapis.com/css2?family=Oswald:wght@600&family=Barlow:wght@400;500&family=Barlow+Semi+Condensed:wght@500&family=Josefin+Sans:wght@300&display=swap" rel="stylesheet">
<style>
  :root {
    --sky: #c8f2ee;
    --mint: #b6ecc9;
    --lime: #b9f04a;
    --paper: #f6fbf4;
    --plum: #2e1a47;
    --plum-soft: #4a2450;
    --pink: #f28bc8;
    --ink: #14141a;
    --sun: #f5c93a;
    --dress: #8a4fc0;
    --hair: #e8934a;
  }
  * { margin: 0; padding: 0; box-sizing: border-box; }
  html, body { width: 1200px; height: 848px; overflow: hidden; background: #fff; }
  .cover {
    position: relative; width: 1200px; height: 848px; overflow: hidden;
    background: linear-gradient(180deg, var(--sky) 0%, var(--sky) 38%, var(--mint) 48%, #d8f3dd 62%, var(--paper) 78%, #fff 100%);
    font-family: "Barlow", sans-serif; color: var(--ink);
  }
  .backdrop { position: absolute; inset: 0; }
  .sun { position: absolute; left: 285px; top: 51px; width: 204px; height: 204px; }
  .dancer { position: absolute; left: 700px; top: 40px; width: 420px; height: 795px; }

  .tagline {
    position: absolute; right: 6px; top: 50px; font-size: 15.2px; font-weight: 500; white-space: nowrap;
  }
  .tagline .values { color: var(--pink); }
  .front-title { position: absolute; left: 661px; top: 106px; width: 522px; }
  .series {
    font-family: "Josefin Sans", sans-serif; font-weight: 300; font-size: 46px; line-height: 1;
    color: var(--plum-soft); letter-spacing: 1px; text-align: center; padding-left: 6px;
  }
  .main-title {
    font-family: "Oswald", sans-serif; font-weight: 600; font-size: 88px; line-height: 1;
    color: var(--plum); letter-spacing: -2.5px; text-transform: uppercase; text-align: center; margin-top: 2px;
  }
  .subtitle {
    font-family: "Barlow Semi Condensed", sans-serif; font-weight: 500; font-size: 21.6px;
    color: var(--pink); white-space: nowrap; margin-top: -4px;
  }

  .blurb { position: absolute; left: 27px; top: 480px; width: 520px; font-size: 12.9px; line-height: 15.9px; font-weight: 500; }
  .blurb p + p, .blurb ul + p, .blurb p + ul { margin-top: 15.9px; }
  .blurb ul { list-style: none; color: var(--pink); }
  .blurb li::before { content: "• "; }

  .spine {
    position: absolute; left: 566px; top: 830px; transform: rotate(-90deg); transform-origin: 0 0;
    white-space: nowrap; display: flex; align-items: baseline; gap: 12px; height: 30px;
  }
  .spine .series-spine { font-family: "Josefin Sans", sans-serif; font-weight: 300; font-size: 22px; color: var(--plum-soft); }
  .spine .title-spine { font-family: "Oswald", sans-serif; font-weight: 600; font-size: 33px; color: var(--plum); letter-spacing: -1px; }
</style>
</head>
<body>
<main class="cover">
  <svg class="backdrop" viewBox="0 0 1200 848" role="img" aria-label="Gemalter Hintergrund mit grünen Sternen, Farbspritzern und hellen Flächen">
    <defs>
      <radialGradient id="glow" cx="0.5" cy="0.5" r="0.5">
        <stop offset="0" stop-color="#d9ff3a" stop-opacity="0.9"/>
        <stop offset="1" stop-color="#b9f04a" stop-opacity="0"/>
      </radialGradient>
    </defs>
    <ellipse cx="820" cy="420" rx="260" ry="300" fill="url(#glow)"/>
    <ellipse cx="900" cy="760" rx="260" ry="110" fill="url(#glow)" opacity="0.7"/>
    <polygon points="0,580 300,520 560,560 560,848 0,848" fill="#fbfdf9" opacity="0.75"/>
    <polygon points="640,720 1200,640 1200,848 640,848" fill="#ffffff" opacity="0.5"/>
  </svg>

  <svg class="sun" viewBox="0 0 204 204" role="img" aria-label="Gemalte gelbe Sonne">
    <circle cx="102" cy="102" r="102" fill="var(--sun)"/>
  </svg>

  <svg class="dancer" viewBox="0 0 420 795" role="img" aria-label="Aquarell-Illustration einer tanzenden Frau im lila Kleid mit rotblondem Haar, die nach oben greift">
    <defs>
      <radialGradient id="dancerDress" cx="0.5" cy="0.5" r="0.5">
        <stop offset="0" stop-color="var(--dress)" stop-opacity="0.75"/>
        <stop offset="0.6" stop-color="var(--dress)" stop-opacity="0.4"/>
        <stop offset="1" stop-color="var(--dress)" stop-opacity="0"/>
      </radialGradient>
      <radialGradient id="dancerHair" cx="0.5" cy="0.5" r="0.5">
        <stop offset="0" stop-color="var(--hair)" stop-opacity="0.55"/>
        <stop offset="1" stop-color="var(--hair)" stop-opacity="0"/>
      </radialGradient>
    </defs>
    <ellipse cx="320" cy="390" rx="110" ry="140" fill="url(#dancerHair)"/>
    <ellipse cx="220" cy="520" rx="200" ry="190" fill="url(#dancerDress)"/>
  </svg>

  <p class="tagline">Durch die Kraft Ihrer Wünsche <span class="values">ERFOLG LIEBE GESUNDHEIT REICHTUM</span> anziehen</p>

  <header class="front-title">
    <p class="series">SUNNY MIND</p>
    <h1 class="main-title">Manifestieren</h1>
    <p class="subtitle">Visualisieren Sie mit dem Gesetz der Anziehung Ihr Leben neu</p>
  </header>

  <div class="spine">
    <span class="series-spine">SUNNY MIND</span>
    <span class="title-spine">MANIFESTIEREN</span>
  </div>

  <section class="blurb">
    <p>Wir sehen immer wieder erfolgreiche Menschen, beispielsweise in den sozialen Medien,<br>und fragen uns:<br>„Was machen diese Menschen anders als ich?“ „Wie entsteht ihr persönlicher Erfolg?“<br>„Was kann ich in meinem Leben verändern, damit ich auch Glück und Erfolg im Alltag erlebe?“</p>
    <p>Manchmal bedarf es gar nicht viel!<br>Doch Sie müssen sich dafür entscheiden diesen Weg zu gehen!</p>
    <p>Dieses Buch bietet Ihnen die Antwort auf Ihre Sehnsüchte und Herzenswünsche.<br>Vielleicht wollten Sie schon immer mal etwas Bestimmtes erfahren, bekommen oder sein,<br>und sind immer wieder gescheitert.</p>
    <ul>
      <li>Mit praktischen Anleitungen werden Sie „step by step“ in Ihr Glück geführt</li>
      <li>Sie bekommen wissenschaftlich erklärte Hintergründe Ihrer Manifestationen</li>
    </ul>
    <p>Sie sind es wert, Ihr volles Potenzial zu leben!<br>Sie sind es wert Liebe, Glück und Geld anzuziehen!<br>Werden Sie zu dem Menschen, der Sie immer sein wollten!</p>
  </section>
</main>
</body>
</html>
```